Value of Working with an Agent

We need a flyer design in standard 8.5x11 format. One side full-color design. I am an agent and will be using this flyer to promote to Skilled Nursing Centers on the Value of working with an insurance agent. I'm looking for an eye-catching flyer that draws the readers attention to the value added services I provide.

Images of the services from their respective companies are provided.
The two focus products providing the services are: 1)Golden Horizons and 2)BVLT Medicare Fullway.

Look and Feel:
Elegant, Professional, Colorful, Eye-Catching

Target Market:
Skilled Nursing Home Managers

Target Market(s)

Industry/Entity Type

Medicare

Font styles to use
Serif

Requirements
Must have
• Content:
• -Medicare only clients can get upgraded benefits with an MAPD plan
• -High rated MAPD plans result in Higher Capitation rates for Skilled Nursing Homes
• -MAPD plans come with KinHelper to help lower-income Medicare patients get help through 2,000 different community assistant programs.
• -All paperwork is handled by the agent. Usually done in 30 mins and patients plans start the very next month.
• -All Medicare patients entering a Skilled Nursing Center are eligible to make any changes needed to their Medicare benefits upon entering the Skilled Nursing Facility.
• -MAPD plans offer a personal case manager for their patients when they leave the Skilled Nursing Home.
• -Patients Benefits included in our MAPD plans: 24hr Nurse Hotline, $200 per year credit for Over-the-Counter items, Chiropractic and Acupuncture Coverage, $0 copay Eye Exams, 2 Dental Cleanings per year. Virtual Doctor Visits, House Call Coverage, $0 monthly premium.
• -Services provided by me are no cost to both the Nursing Home and the patient.
• -Agent information: Name: Brent Kowalczyk Phone: (555)318-7260 Email: b.kowalczyk@trellisbayins.example
• Images of the services from their respective companies are provided.
• The two focus products providing the services are: 1)Golden Horizons and 2)BVLT Medicare Fullway.

```html
<!DOCTYPE html>
<html lang="en">
<head>
<meta charset="utf-8">
<title>Value of Working with an Agent</title>
<link href="https://fonts.googleapis.com/css2?family=Montserrat:ital,wght@0,400;0,500;0,700;1,400&display=swap" rel="stylesheet">
<style>
  :root{
    --red:#c8102e;
    --red-bright:#e0192f;
    --red-deep:#8e0f1c;
    --maroon:#5a0d14;
    --white:#ffffff;
    --pink:#f7d6d9;
    --photo-a:#6f6a66;
    --photo-b:#b9a993;
    --photo-c:#d9d4cf;
    --strip:#f4f4f4;
    --logo-ink:#3a3f4a;
  }
  *{box-sizing:border-box;margin:0;padding:0}
  html,body{width:928px;height:1200px;overflow:hidden;background:#fff}
  body{font-family:"Montserrat",Arial,sans-serif;color:var(--white)}
  .flyer{position:relative;width:928px;height:1200px;overflow:hidden;background:var(--red)}

  .hero-photo{position:absolute;left:0;top:150px;width:928px;height:520px;
    background:linear-gradient(100deg,var(--photo-a) 0%,var(--photo-b) 45%,var(--photo-c) 75%,#eeeeee 100%)}
  .hero-shade{position:absolute;left:0;top:150px;width:928px;height:520px;
    background:linear-gradient(90deg,rgba(60,40,35,.55),rgba(60,40,35,.15) 70%,rgba(0,0,0,0))}
  .header-wave{position:absolute;left:0;top:0;width:928px;height:260px}

  .brand{position:absolute;left:66px;top:44px;display:flex;align-items:center;gap:12px}
  .brand-dot{width:72px;height:72px;border-radius:50%;border:3px solid var(--white)}
  .brand-name{font-size:15px;font-weight:500;line-height:1.3;color:var(--white)}

  .id-card{position:absolute;left:586px;top:36px;width:258px;height:172px;border-radius:8px;
    background:linear-gradient(180deg,#f3f4f8 0%,#e5e7ee 100%);box-shadow:0 4px 12px rgba(0,0,0,.35);transform:rotate(-2deg)}

  .points-rail{position:absolute;left:38px;top:271px;width:42px;height:352px;background:var(--red)}
  .points{position:absolute;left:38px;top:276px;width:860px;list-style:none}
  .points li{position:relative;padding-left:69px;font-size:17.5px;font-weight:500;line-height:1.3;
    text-shadow:0 1px 3px rgba(0,0,0,.55);margin-bottom:21px}
  .points svg{position:absolute;left:6px;top:0;width:30px;height:30px}

  .partner-strip{position:absolute;left:0;top:670px;width:928px;height:117px;background:var(--strip);
    display:flex;align-items:center;justify-content:space-around;padding:0 20px}
  .partner{display:flex;align-items:center;gap:6px;font-size:13px;font-weight:700;color:var(--logo-ink);white-space:nowrap}
  .partner i{display:block;width:14px;height:14px;background:var(--red)}
  .partner .c{border-radius:50%;background:#1f6fb4}

  .benefits{position:absolute;left:0;top:787px;width:928px;height:263px;
    background:radial-gradient(ellipse at 70% 30%,var(--red-bright),var(--red) 60%,var(--red-deep))}
  .benefits h2{text-align:center;font-size:22px;font-weight:700;margin-top:30px;letter-spacing:.2px}
  .benefits hr{border:0;border-top:1.5px solid var(--white);width:800px;margin:12px auto 0}
  .benefit-cols{display:flex;justify-content:space-between;padding:10px 126px 0 84px}
  .benefit-cols ul{list-style:none}
  .benefit-cols li{font-size:16.5px;color:var(--pink);line-height:29px}
  .no-cost{text-align:center;font-style:italic;font-size:18.5px;margin-top:14px}

  .agent{position:absolute;left:0;top:1050px;width:928px;height:150px;background:var(--maroon)}
  .agent-photo{position:absolute;left:60px;top:2px;width:152px;height:148px;
    background:linear-gradient(160deg,#9a8a7e,#3b3433)}
  .agent-name{position:absolute;left:245px;top:34px;font-size:18.5px;font-weight:700}
  .agent-phone{position:absolute;left:245px;top:72px;font-size:16px}
  .agent-email{position:absolute;left:245px;top:104px;font-size:16px}
  .agent-web{position:absolute;left:575px;top:104px;font-size:16.5px;font-weight:700}
</style>
</head>
<body>
<main class="flyer">
  <div class="hero-photo" role="img" aria-label="Photo of an agent meeting with a senior couple at a table"></div>
  <div class="hero-shade"></div>

  <svg class="header-wave" viewBox="0 0 928 260" aria-hidden="true">
    <defs>
      <linearGradient id="hdr" x1="0" x2="1">
        <stop offset="0" stop-color="#8e0f1c"/>
        <stop offset=".5" stop-color="#c8102e"/>
        <stop offset="1" stop-color="#e0192f"/>
      </linearGradient>
    </defs>
    <path d="M0 0H928V130C760 150 420 190 0 245Z" fill="url(#hdr)"/>
    <path d="M0 245C420 190 760 150 928 130V142C760 162 420 202 0 258Z" fill="#ffffff" opacity=".85"/>
  </svg>

  <div class="brand">
    <span class="brand-dot"></span>
    <span class="brand-name">Trellis Bay<br>Insurance Exchange</span>
  </div>

  <div class="id-card" role="img" aria-label="Sample health insurance member card"></div>

  <div class="points-rail"></div>
  <ul class="points">
    <li><svg viewBox="0 0 30 30" fill="none" stroke="#fff" stroke-width="2.4" stroke-linecap="round"><path d="M8 26C8 14 14 9 22 9"/><path d="M17 4l6 5-6 5"/></svg>Medicare only clients can get upgraded benefits with an MAPD plan</li>
    <li><svg viewBox="0 0 30 30" fill="none" stroke="#fff" stroke-width="2.2" stroke-linecap="round"><path d="M4 7h4M4 14h4M4 21h4M12 7h14M12 14h14M12 21h14"/></svg>High rated MAPD plans result in Higher Capitation rates for Skilled Nursing Homes</li>
    <li><svg viewBox="0 0 30 30" fill="none" stroke="#fff" stroke-width="2.2" stroke-linecap="round"><path d="M3 14C3 7 27 7 27 14Z" fill="#fff"/><path d="M15 14v10a3 3 0 0 1-6 0"/></svg>MAPD plans come with KinHelper to help lower-income Medicare patients get help through 2,000 different community assistant programs.</li>
    <li><svg viewBox="0 0 30 30"><circle cx="15" cy="15" r="13" fill="#fff"/><text x="15" y="19.5" text-anchor="middle" font-size="12" font-weight="700" fill="#c8102e" font-family="Montserrat,Arial,sans-serif">30</text></svg>All paperwork is handled by the agent. Usually done in 30 mins and patients plans start the very next month.</li>
    <li><svg viewBox="0 0 30 30" fill="none" stroke="#fff" stroke-width="2.2" stroke-linecap="round"><circle cx="15" cy="15" r="13"/><path d="M10 20l10-10M10 20l-1 2 2-1"/></svg>All Medicare patients entering a Skilled Nursing Center are eligible to make any changes needed to their Medicare benefits upon entering the Skilled Nursing Facility.</li>
    <li><svg viewBox="0 0 30 30" fill="none" stroke="#fff" stroke-width="2.2" stroke-linecap="round"><circle cx="15" cy="15" r="13"/><path d="M8 15l4 4 10-9"/></svg>MAPD plans offer a personal case manager for their patients when they leave the Skilled Nursing Home.</li>
  </ul>

  <section class="partner-strip">
    <span class="partner"><i></i>Golden Horizons</span>
    <span class="partner"><i></i>BVLT Medicare Fullway</span>
    <span class="partner">KinHelper</span>
    <span class="partner"><i class="c"></i>Northpoint Medical</span>
    <span class="partner">Clinova</span>
    <span class="partner"><i class="c" style="background:#1e8a4c"></i>Regional RideCare Network</span>
  </section>

  <section class="benefits">
    <h2>PATIENTS BENEFITS INCLUDED IN OUR MAPD PLANS:</h2>
    <hr>
    <div class="benefit-cols">
      <ul>
        <li>24hr Nurse Hotline,</li>
        <li>$200 per year credit for Over-the-Counter items,</li>
        <li>Chiropractic and Acupuncture Coverage,</li>
        <li>$0 copay Eye Exams,</li>
      </ul>
      <ul>
        <li>2 Dental Cleanings per year.</li>
        <li>Virtual Doctor Visits,</li>
        <li>House Call Coverage,</li>
        <li>$0 monthly premium.</li>
      </ul>
    </div>
    <p class="no-cost">Services provided by me are no cost to both the Nursing Home and the patient.</p>
  </section>

  <footer class="agent">
    <div class="agent-photo" role="img" aria-label="Portrait photo of the agent"></div>
    <p class="agent-name">BRENT KOWALCZYK</p>
    <p class="agent-phone">(555)318-7260</p>
    <p class="agent-email">b.kowalczyk@trellisbayins.example</p>
    <p class="agent-web">WWW.TRELLISBAYINS.EXAMPLE</p>
  </footer>
</main>
</body>
</html>
```